Home page and features page design for SaaS company

We're looking for designs for a home page and a features page of a new website (possibly more pages to be commissioned thereafter). The website is called 'Brightly Afloat' and is a service that helps swimming clubs and schools reduce administration.

The website will have a clean, minimalist, modern feel but not corporate. Here's an idea of the type of style: https://squadlio.net/pages/payments

At the top of the home page (above the fold) will show the two personas that the website is targeting (Swimming clubs and Swimming Schools) on a styled background (no cheesy stock images please!). Those personas can be represented as an illustration (see page 2 for an example), line art graphic or icon and will link through to a features page.

For your information, the type of people that are members of swimming clubs include beginners, competitive squads and adult swimmers. People that attend a swimming school are typically children learning to swim. If you can represent the above in simple line art illustrations/graphics/icons that match the style of our logo - great!

Below the fold on the home page will be an illustration of the main functions of the site (with our logo central to that) and at the bottom of the page will be what they get for free, testimonials and a call to action for booking a demo.

I've attached a simple wireframe of the home page for your information.

The second page is the features page. This summarises the benefits of each major feature. Each feature listed on the page is separated by a call to action. Here's a link to the content of the features page: http://webhost4.qarvik-advisory.com/KLTsalespages/swimming/swim-club-management-software.html

Don't take a lead from the look / feel / design of this page. I don't like it (hence I'm on here to find a better design!). One thing I'd like to incorporate is a snippet preview of a screenshot on the features page (a bit like in the example). The user can click on this and the full screenshot will load in a pop-up.

The style of the features page should flow from the home page.
Updates

Project Deadline Extended
Reason: Extending deadline to allow more quality designs and give those that have submitted time to make any revisions.

Target Market(s)

Swimming clubs and swimming schools

Industry/Entity Type

Internet

Number of Pages Required

2 page

Font styles to use
Sans Serif

Colors
33a6d7
33b8a4

Requirements
Must have
• Clean, minimalist, modern feel but not corporate. Here's an idea of the type of style: https://squadlio.net/pages/payments
Should not have
• Unstylised stock photographs

```html
<!DOCTYPE html>
<html lang="en">
<head>
<meta charset="utf-8">
<title>Brightly Afloat – Membership Software For Swimming Clubs And Schools</title>
<link href="https://fonts.googleapis.com/css2?family=Raleway:ital,wght@0,400;0,500;0,600;0,700;1,400&display=swap" rel="stylesheet">
<style>
:root{
  --blue:#33a6d7;
  --blue-deep:#1f8fc8;
  --teal:#33b8a4;
  --ink:#333333;
  --text:#555555;
  --muted:#777777;
  --line:#dddddd;
  --panel:#f2f2f2;
  --section:#f8f8f8;
  --white:#ffffff;
  --footer:#333333;
}
*{box-sizing:border-box;margin:0;padding:0}
html,body{width:1200px;height:2413px;overflow:hidden}
body{position:relative;font-family:"Raleway",Arial,sans-serif;color:var(--text);background:var(--white)}
.abs{position:absolute}

/* Header */
.site-header{position:absolute;left:0;top:0;width:1200px;height:75px;background:var(--white)}
.brand{position:absolute;left:88px;top:22px;display:flex;align-items:center;gap:10px}
.brand-dot{width:30px;height:30px;border-radius:50%;background:var(--blue)}
.brand-name{font-size:27px;font-weight:700;color:var(--blue)}
.main-nav a{position:absolute;top:30px;font-size:14.5px;font-weight:500;color:var(--ink);text-decoration:none}
.btn-signin{position:absolute;left:1017px;top:19px;width:96px;height:37px;background:var(--teal);color:var(--white);font-size:14px;font-weight:600;display:flex;align-items:center;justify-content:center}

/* Hero */
.hero{position:absolute;left:0;top:75px;width:1200px;height:496px;background:radial-gradient(ellipse at 50% 55%,#4a5862 0%,#2e3a42 45%,#1d2429 100%)}
.hero-title{position:absolute;left:0;top:52px;width:1200px;text-align:center;color:var(--white);font-size:32px;font-weight:600}
.persona{position:absolute;top:129px;width:356px;height:320px}
.persona-art{position:absolute;left:0;top:0;width:100%;height:190px;border-radius:24px;background:linear-gradient(180deg,rgba(215,218,221,.9) 0%,rgba(200,205,209,.85) 100%)}
.persona-name{position:absolute;left:0;width:100%;top:213px;text-align:center;color:var(--white);font-size:30px;font-weight:600}
.btn-more{position:absolute;top:269px;left:114px;width:127px;height:39px;background:var(--white);color:var(--teal);font-size:13px;font-weight:600;display:flex;align-items:center;justify-content:center}

/* Section headings */
.section-title{position:absolute;left:0;width:1200px;text-align:center;font-size:28px;font-weight:600;color:var(--blue)}
.rule{position:absolute;left:412px;width:376px;height:1px;background:var(--line)}
.rule::after{content:"";position:absolute;left:164px;top:-1px;width:48px;height:3px;background:var(--blue)}
.title-teal{color:var(--teal)}

/* Features diagram */
.feature-map{position:absolute;left:0;top:571px;width:1200px;height:528px}
.node-label{position:absolute;font-size:15px;font-weight:500;color:var(--blue);white-space:nowrap}
.node-label.right{text-align:right}
.node-label.active{color:var(--teal)}
.coach{position:absolute;left:965px;top:53px;width:177px;height:425px;border-radius:80px 80px 30px 30px;background:linear-gradient(180deg,#3a9fd6 0%,#f1d3b4 35%,#ffffff 55%,#2e8fc4 80%,#e53b3b 100%)}

/* Feature products */
.products{position:absolute;left:0;top:1099px;width:1200px;height:405px;background:var(--section);border-top:1px solid #eeeeee}
.product{position:absolute;width:427px;height:109px;background:var(--panel);padding:20px 22px}
.product h3{font-size:21px;font-weight:600;color:var(--blue);margin-bottom:8px}
.product p{font-size:11px;line-height:18px;color:var(--ink);white-space:nowrap}
.product.right{text-align:right}
.product-center{position:absolute;left:528px;top:185px;width:145px;height:109px;background:var(--white);display:flex;align-items:center;justify-content:center;text-align:center;font-size:17px;font-weight:700;color:var(--blue)}

/* CTA */
.cta{position:absolute;left:0;top:1504px;width:1200px;height:134px;background:var(--blue)}
.cta h2{position:absolute;left:311px;top:44px;font-size:34px;font-weight:600;color:var(--white)}
.btn-book{position:absolute;left:742px;top:47px;width:145px;height:42px;background:var(--ink);color:var(--white);font-size:15px;font-weight:600;display:flex;align-items:center;justify-content:center}

/* Testimonials */
.testimonials{position:absolute;left:0;top:1638px;width:1200px;height:413px;background:var(--white)}
.quote-card{position:absolute;top:119px;width:426px;height:198px}
.quote-card svg{position:absolute;left:0;top:0}
.quote-text{position:absolute;left:34px;top:22px;width:370px;font-size:11px;line-height:18px;font-style:italic;color:var(--ink)}
.quote-mark{position:absolute;font-size:42px;line-height:1;color:#cccccc;font-family:Georgia,serif}
.avatar{position:absolute;top:148px;left:24px;width:96px;height:96px;border-radius:50%;border:4px solid var(--white);box-shadow:0 0 0 1px #e2e2e2}
.quote-name{position:absolute;top:218px;left:196px;font-size:12px;font-weight:600;color:var(--ink)}
.slider-arrow{position:absolute;top:200px}

/* Contact */
.contact{position:absolute;left:0;top:2051px;width:1200px;height:326px;background:#f5f5f5}
.contact-intro{position:absolute;left:0;top:118px;width:1200px;text-align:center;font-size:11.5px;line-height:21px;color:var(--muted);white-space:nowrap}
.field{position:absolute;height:26px;background:var(--white);border:1px solid #d8d8d8;border-radius:3px;font-size:10px;color:var(--ink);padding:6px 8px}
.btn-submit{position:absolute;left:172px;top:271px;width:98px;height:29px;background:var(--blue);color:var(--white);font-size:13px;font-weight:500;display:flex;align-items:center;justify-content:center}
.info{position:absolute;left:837px;font-size:11.5px;line-height:17px;color:var(--muted);white-space:nowrap}
.info svg{position:absolute;left:0;top:2px}
.info span{display:block;margin-left:24px}

/* Footer */
.site-footer{position:absolute;left:0;top:2377px;width:1200px;height:36px;background:var(--footer)}
.copyright{position:absolute;left:161px;top:11px;font-size:11.5px;color:#dddddd}
.social{position:absolute;top:7px;width:22px;height:22px;border-radius:50%;background:var(--white)}
</style>
</head>
<body>

<header class="site-header">
  <div class="brand"><span class="brand-dot"></span><span class="brand-name">Brightly Afloat</span></div>
  <nav class="main-nav">
    <a style="left:481px">About Us</a>
    <a style="left:576px">Pricing</a>
    <a style="left:655px">Free Resources</a>
    <a style="left:790px">Free Account</a>
    <a style="left:912px">Contact Us</a>
  </nav>
  <div class="btn-signin">SIGN IN</div>
</header>

<section class="hero" role="img" aria-label="Darkened photo of a swimmer doing front crawl, water spraying">
  <h1 class="hero-title">Membership Software For Swimming Clubs And Schools</h1>

  <div class="persona" style="left:191px">
    <div class="persona-art" role="img" aria-label="Illustration of a club swimmer over waves"></div>
    <div class="persona-name">Swimming Clubs</div>
    <div class="btn-more">Find Out More</div>
  </div>

  <div class="persona" style="left:653px">
    <div class="persona-art" role="img" aria-label="Illustration of a group of children swimming"></div>
    <div class="persona-name">Swimming Schools</div>
    <div class="btn-more">Find Out More</div>
  </div>
</section>

<section class="feature-map">
  <h2 class="section-title" style="top:38px">Why Choose Us</h2>
  <div class="rule" style="top:85px"></div>

  <svg class="abs" style="left:0;top:0" width="1200" height="528" viewBox="0 0 1200 528">
    <g fill="none" stroke="#cfd8dc" stroke-width="1.5">
      <circle cx="600" cy="303" r="68" fill="#fff" stroke="#e3e3e3"/>
      <path d="M600 226v-14M548 253l-10-10M652 253l10-10M522 303h-14M678 303h14M548 353l-10 10M652 353l10 10M600 380v14"/>
    </g>
    <g fill="#fff" stroke="var(--blue)" stroke-width="1.6">
      <circle cx="600" cy="176" r="27"/>
      <circle cx="496" cy="222" r="27"/>
      <circle cx="694" cy="222" r="27"/>
      <circle cx="729" cy="303" r="27"/>
      <circle cx="496" cy="380" r="27"/>
      <circle cx="694" cy="380" r="27"/>
      <circle cx="600" cy="427" r="27"/>
    </g>
    <circle cx="463" cy="303" r="28" fill="var(--teal)"/>
    <g fill="var(--blue)">
      <circle cx="471" cy="222" r="3"/><circle cx="669" cy="222" r="3"/>
      <circle cx="704" cy="303" r="3"/><circle cx="471" cy="380" r="3"/>
      <circle cx="669" cy="380" r="3"/>
    </g>
    <circle cx="436" cy="303" r="3" fill="var(--teal)"/>
    <g fill="none" stroke="var(--blue)" stroke-width="1.6">
      <rect x="588" y="166" width="24" height="20" rx="2"/><path d="M588 172h24M592 180h8"/>
      <rect x="486" y="210" width="20" height="24" rx="1"/><path d="M490 216h12M490 221h12M490 226h8"/>
      <rect x="684" y="210" width="20" height="24" rx="1"/><path d="M689 229v-6M694 229v-10M699 229v-4"/>
      <circle cx="729" cy="303" r="11"/><path d="M723 303h12M729 297v12"/>
      <rect x="486" y="368" width="20" height="24" rx="1"/><path d="M486 375h20M490 381h12M490 386h12"/>
      <rect x="682" y="371" width="24" height="18" rx="1"/><path d="M682 371l12 10 12-10"/>
      <path d="M586 432q7-5 14 0t14 0M586 438q7-5 14 0t14 0"/><circle cx="606" cy="421" r="3"/>
    </g>
    <g fill="none" stroke="#fff" stroke-width="1.8">
      <rect x="451" y="294" width="24" height="18" rx="2"/><path d="M456 300h14M456 306h9"/>
    </g>
  </svg>

  <div class="abs" style="left:532px;top:290px;width:136px;text-align:center;font-size:16px;font-weight:700;color:var(--blue)">Brightly Afloat</div>

  <div class="node-label" style="left:538px;top:115px;width:124px;text-align:center">Online Payments</div>
  <div class="node-label right" style="left:255px;top:213px;width:200px">Online Registrations</div>
  <div class="node-label" style="left:739px;top:213px">Financial Reporting</div>
  <div class="node-label right active" style="left:218px;top:294px;width:200px">Attendance Register</div>
  <div class="node-label" style="left:774px;top:294px">Membership Data</div>
  <div class="node-label right" style="left:255px;top:371px;width:200px">Event Management</div>
  <div class="node-label" style="left:739px;top:371px">Group Email</div>
  <div class="node-label" style="left:538px;top:469px;width:124px;text-align:center">Galas</div>

  <div class="coach" role="img" aria-label="Cartoon swimming coach with cap, whistle and stopwatch"></div>
</section>

<section class="products">
  <h2 class="section-title title-teal" style="top:40px">Feature Products</h2>
  <div class="rule" style="top:88px"></div>

  <div class="product" style="left:161px;top:119px">
    <h3>Access To Exclusive Tools</h3>
    <p>We have over 100 great features and functions to help cut<br>down admin and increase payment collection.</p>
  </div>
  <div class="product right" style="left:611px;top:119px">
    <h3>Account Setup</h3>
    <p>We take time to understand how your club works and set<br>your account to maximise efficiencies.</p>
  </div>
  <div class="product" style="left:161px;top:251px">
    <h3>Software Updates</h3>
    <p>We continuously listen to our clients and develop functionality<br>in line with their feedback to help you improve efficiencies and save time.</p>
  </div>
  <div class="product right" style="left:611px;top:251px">
    <h3>First Class Support</h3>
    <p>From your first training session to on-going support, we're here to help<br>you get the best from the system. You can reach us by chat, email or video call</p>
  </div>
  <div class="product-center">Brightly<br>Afloat</div>
</section>

<section class="cta">
  <h2>Book A Free Demo Now</h2>
  <div class="btn-book">BOOK NOW</div>
</section>

<section class="testimonials">
  <h2 class="section-title" style="top:38px;color:var(--teal)">Client Testimonial</h2>
  <div class="rule" style="top:87px"></div>

  <svg class="slider-arrow" style="left:123px" width="12" height="22" viewBox="0 0 12 22"><path d="M11 1L1 11l10 10" fill="none" stroke="#cccccc" stroke-width="1.5"/></svg>
  <svg class="slider-arrow" style="left:1065px" width="12" height="22" viewBox="0 0 12 22"><path d="M1 1l10 10L1 21" fill="none" stroke="#cccccc" stroke-width="1.5"/></svg>

  <div class="quote-card" style="left:161px">
    <svg width="426" height="200" viewBox="0 0 426 200"><path d="M6 1h414a5 5 0 0 1 5 5v180a5 5 0 0 1-5 5H330l-18 8-6-8H6a5 5 0 0 1-5-5V6a5 5 0 0 1 5-5z" fill="#fff" stroke="#e2e2e2"/></svg>
    <span class="quote-mark" style="left:34px;top:16px">&ldquo;</span>
    <p class="quote-text">&nbsp;&nbsp;&nbsp;&nbsp;&nbsp;&nbsp;&nbsp;Lorem Ipsum is simply dummy text of the printing and typeseng industry. Lorem Ipsum has been the industry's standard dummy text ever since the 1500s, when an unknown printer took a galley of type and scrambled it to make a type specimen book. It has survived type specien book. It has survived not only five centuries, but ot only five centuries, but also the leap into electc typesetting, remaining essentially.</p>
    <span class="quote-mark" style="left:330px;top:118px">&rdquo;</span>
    <div class="avatar" style="background:linear-gradient(160deg,#8c9aa6,#4f6a86)" role="img" aria-label="Portrait photo of a male client"></div>
    <div class="quote-name">- Lorem Ipsum Dolor</div>
  </div>

  <div class="quote-card" style="left:621px;width:417px">
    <svg width="417" height="200" viewBox="0 0 417 200"><path d="M6 1h405a5 5 0 0 1 5 5v180a5 5 0 0 1-5 5H330l-18 8-6-8H6a5 5 0 0 1-5-5V6a5 5 0 0 1 5-5z" fill="#fff" stroke="#e2e2e2"/></svg>
    <span class="quote-mark" style="left:34px;top:16px">&ldquo;</span>
    <p class="quote-text">&nbsp;&nbsp;&nbsp;&nbsp;&nbsp;&nbsp;&nbsp;Lorem Ipsum is simply dummy text of the printing and typeseng industry. Lorem Ipsum has been the industry's standard dummy text ever since the 1500s, when an unknown printer took a galley of type and scrambled it to make a type specimen book. It has survived type specien book. It has survived not only five centuries, but ot only five centuries, but also the leap into electc typesetting, remaining essentially.</p>
    <span class="quote-mark" style="left:330px;top:118px">&rdquo;</span>
    <div class="avatar" style="background:linear-gradient(160deg,#e4c9a8,#b98a5e)" role="img" aria-label="Portrait photo of a smiling female client"></div>
    <div class="quote-name">- Lorem Ipsum Dolor</div>
  </div>
</section>

<section class="contact">
  <h2 class="section-title" style="top:38px;color:var(--teal)">Client Testimonial</h2>
  <div class="rule" style="top:87px"></div>
  <p class="contact-intro">Lorem Ipsum is simply dummy text of the printing and typesetting industry. Lorem Ipsum has been the industry's standard dummy text ever since the 1500s,<br>when an unknown printer took a galley of type and scrambled it to make a type specimen book.</p>

  <div class="field" style="left:172px;top:169px;width:201px">Your Name</div>
  <div class="field" style="left:383px;top:169px;width:201px">Your Email</div>
  <div class="field" style="left:595px;top:169px;width:201px">Your Subject</div>
  <div class="field" style="left:172px;top:203px;width:624px;height:55px">Message</div>
  <div class="btn-submit">Submit</div>

  <div class="info" style="top:174px">
    <svg width="12" height="14" viewBox="0 0 12 14"><path d="M6 1a4.5 4.5 0 0 0-4.5 4.5C1.5 9 6 13 6 13s4.5-4 4.5-7.5A4.5 4.5 0 0 0 6 1z" fill="var(--ink)"/><circle cx="6" cy="5.5" r="1.6" fill="#f5f5f5"/></svg>
    <span>Lorem Ipsum is simply dummy<br>text of the printing and typestting<br>ind. industry's standard dummy.</span>
  </div>
  <div class="info" style="top:227px">
    <svg width="12" height="13" viewBox="0 0 12 13"><path d="M2 1l3 .3 1 3-1.6 1.2a7 7 0 0 0 3.2 3.2L8.8 7l3 1 .2 3-1.5 1.5C5.5 12 0 6.5.5 1.5z" fill="var(--ink)"/></svg>
    <span>123-456-7890</span>
  </div>
  <div class="info" style="top:254px">
    <svg width="13" height="13" viewBox="0 0 13 13"><rect x="3" y="0.5" width="7" height="4" fill="none" stroke="var(--ink)"/><rect x="0.5" y="4.5" width="12" height="5" rx="1" fill="var(--ink)"/><rect x="3" y="8.5" width="7" height="4" fill="#f5f5f5" stroke="var(--ink)"/></svg>
    <span>(123) 456 - 7890</span>
  </div>
  <div class="info" style="top:282px">
    <svg width="13" height="10" viewBox="0 0 13 10"><rect x="0.5" y="0.5" width="12" height="9" fill="var(--ink)"/><path d="M0.5 0.5l6 5 6-5" fill="none" stroke="#f5f5f5"/></svg>
    <span>info@brightlyafloat.com</span>
  </div>
</section>

<footer class="site-footer">
  <div class="copyright">© 2017 Brightly Afloat. All Rights Reserved.</div>
  <span class="social" style="left:951px"></span>
  <span class="social" style="left:983px"></span>
  <span class="social" style="left:1016px"></span>
</footer>

</body>
</html>
```